Stationary Design for an engineering start-up.

Company name: Lumetra Plank Inc.

Our advanced materials company utilizes a patented process to spray-coat wood surfaces with metal. Metal is sprayed as a super-heated powder and fully conforms to the surface of the wood allowing for a wide range of applications. Metals used are COPPER and BRONZE.

We need a stationary package that includes Business Card, Letter Head, and Envelope.

- After we will submit a contest for a brochure design, so a winning designer will have advantage to take that project as well.

Target Market(s)

Our target market are building and industrial design professionals.

- Architects
- Designers
- Builders

Industry/Entity Type

Engineering

Requirements
Must have
• - All stationary must include our logo (attached)

Sizes:
Business card: Standard 3.5 by 2 inches. Landscape.

Letterhead: 8.5" x 11"

Envelopes:
One standard commercial size #10 (4 1/8" by 9 1/2")
One catalog size envelope (9" by 12")
Assume envelopes are one-sided (front print only)

- Use bleeds where applicable

- Include all fonts used.

File Format:
AI or PSD
** for letterhead please include MSWord template.
Nice to have
• Design style
- Take design style from our logo and attached images.
- Modern, sharp, minimalistic
- Sans fonts
- Don''t be afraid to use color background for business card.
We''re open to ideas of making the business card somehow representative of the product - metal coated wood.

```html
<!DOCTYPE html>
<html lang="en">
<head>
<meta charset="utf-8">
<title>Lumetra Plank Inc. — Letterhead</title>
<link rel="stylesheet" href="https://fonts.googleapis.com/css2?family=Barlow:wght@400;500&family=Montserrat:wght@400;700&display=swap">
<style>
  :root {
    --copper: #f05a28;
    --sand: #bcae95;
    --ink: #7b7b7b;
    --paper: #ffffff;
  }
  html, body {
    margin: 0;
    padding: 0;
    width: 927px;
    height: 1200px;
    overflow: hidden;
    background: var(--paper);
  }
  .letterhead {
    position: relative;
    width: 927px;
    height: 1200px;
    background: var(--paper);
  }
  .masthead {
    position: absolute;
    top: 92px;
    display: flex;
    flex-direction: column;
    font-family: "Montserrat", sans-serif;
    font-size: 11.5px;
    line-height: 18px;
    letter-spacing: 0.07em;
    color: var(--sand);
  }
  .masthead--company { left: 182px; }
  .masthead--contact { left: 364px; }
  .masthead__title {
    color: var(--copper);
    font-weight: 700;
    letter-spacing: 0.16em;
    text-transform: uppercase;
  }
  .masthead__label {
    color: var(--copper);
    font-weight: 700;
    font-size: 9.5px;
    letter-spacing: 0.14em;
    margin-left: 5px;
    text-transform: uppercase;
  }
  .brand-mark {
    position: absolute;
    left: 62px;
    top: 312px;
    width: 70px;
    text-align: center;
    font-family: "Barlow", sans-serif;
    font-weight: 500;
    font-size: 12px;
    line-height: 14px;
    color: var(--copper);
  }
  .recipient {
    position: absolute;
    left: 182px;
    top: 285px;
    margin: 0;
    font-family: "Barlow", sans-serif;
    font-style: normal;
    font-size: 14px;
    line-height: 21.2px;
    color: var(--copper);
  }
  .letter-body {
    position: absolute;
    left: 182px;
    top: 395px;
    width: 640px;
    font-family: "Barlow", sans-serif;
    font-size: 13px;
    line-height: 19.6px;
    color: var(--ink);
  }
  .letter-body p { margin: 0 0 13.3px; }
</style>
</head>
<body>
<main class="letterhead">
  <header>
    <div class="masthead masthead--company">
      <span class="masthead__title">Lumetra Plank Inc.</span>
      <span>48 Cedar Row</span>
      <span>Winnipeg, MB&nbsp; R3C 0V8</span>
    </div>
    <div class="masthead masthead--contact">
      <span class="masthead__title">lumetraplank.com</span>
      <span>204.555.0187<span class="masthead__label">Tel</span></span>
      <span>204.555.0142<span class="masthead__label">Fax</span></span>
    </div>
  </header>

  <div class="brand-mark">Lumetra Plank</div>

  <address class="recipient">
    Dana Whitlock<br>
    Riverbend Community Group<br>
    Unit 4 - 22 Larchmont Place,<br>
    Winnipeg, MB, Canada&nbsp; R2K 3J7
  </address>

  <section class="letter-body">
    <p>Dear Sir,</p>
    <p>Vit volupta quisti nonsed quis unt quam fugitiatia inum non rent doluptatenis ma doluptio maxim ut prempor essinciam landa quo ducipiet omnitatus, non re planist otatem nonse assim sequi ut quati auda cum, ommolut omnis etur atis esequo de pedit audiaer iosapellant explit ullecea turiatus doluptatur sedi odit eiciisqui omnihil iquunt eos doluptis volendae. Neque nat et qui nihilitem. Ita parundis estianditate iducit aut quam facipis eaquis distrum volupta testorest omni omnimol upitatibust, sant.</p>
    <p>Dolo expero beari cus rerehent pellorem sam, tem alia pa velestrum excepersped ea cores et pa nostibus quodita temolup tatemporepe mi, ut etur re lam repro dolorem osantia dipitatur aut aditios aut deratiis aut eostibus dunt faccdolupta tquidestiani vellaut molendi rerrum ium ipsam derferrorro eaquam, omni voluptame venist, iduntem apedi rentiis magnametur ma num et debis ex eossimperum essinum quam, optur rem as sunto denectatio dolorpo ruptat lic tet quossed ea exerrum quatest velland enimus ex erspient es si to di aces venihil idenes sene nam, aturibea dolorporem quiam iducia pero mi, que conseca essiti beatemque verro mod ea aut aces vella quia nonsectat.</p>
    <p>Ignatiatem sum aceatem quaturi aut ipiciis acia is mi, quiatem el eaquodi cuptio essitasperum faccum eum fuga. Nam repta aboruptiunt deriore mpedis simpedi pisquibus.</p>
    <p>Ic torepe optate coremqui aut estendit moluptam repres earchit quo bla que vollorem idit omnisciento ent quae eumquatur magnam voluptatem elibus experibus molorerio. Parum re velitio. Aperupt atemoluptis nonse sit, et doluptatem fugiatu reperro blabore ntibus, consequam nonsequi derrovita con cum ilibusam rernam quias doluptust, officto tatist ut autas etur re coressitis doluptiisti nonsed untibusdam faccusae cus voluptam fugiatem arit qui totaquidi ulparum enditat quaerrovides re magni ut maximol uptatesciur? Quat.</p>
    <p>Event es aboribus maio etur, te nonet occum untios es dolor autatem ipiciiscil iunt modi tectorem illo quae ipsant abo. Ita illanti nverum quationectur apicatisi reperibero magnistium resecus.</p>
  </section>
</main>
</body>
</html>
```